Calbrook Partners needs new business cards

Please refer to brief for logo design and use design #2447418. I would like to see a few concepts as I may not always go to print with full colour backing. At front of card I'd like to include staff name, company name and contact details. At back of card I'd like to include a tag line and list of services.
Updates

Reason: I have extended the deadline because I'm still hoping to receive the ideal business card for Calbrook Partners

Target Market(s)

Middle to senior executives within corporate sector. Top end of town eg, telcos, banks, large hospitals, technology companies.

Requirements
Must have
• Design #2447418 logo and colours
Nice to have
• the back of the card can be as creative as the concept you already submitted, which was quite nice.
Should not have
• Not too busy or cluttered, bearing in mind original logo brief

```html
<!DOCTYPE html>
<html lang="en">
<head>
<meta charset="utf-8">
<title>Calbrook Partners – Business Cards</title>
<link href="https://fonts.googleapis.com/css2?family=Oxygen:wght@400;700&display=swap" rel="stylesheet">
<style>
  :root {
    --navy: #2f2a7c;
    --cyan: #0aa3dc;
    --royal: #3b4fe0;
    --ink: #111118;
    --paper: #ffffff;
    --backdrop: #dcdde8;
  }
  * { box-sizing: border-box; margin: 0; padding: 0; }
  html, body { width: 1200px; height: 1000px; overflow: hidden; }
  body {
    background: var(--backdrop);
    font-family: "Oxygen", "Helvetica Neue", Arial, sans-serif;
    position: relative;
  }
  .card {
    position: absolute;
    width: 570px;
    height: 330px;
    overflow: hidden;
    box-shadow: 0 6px 18px rgba(30, 28, 90, 0.25);
  }
  .card--front { background: var(--paper); }
  .card--centered { left: 20px; top: 70px; }
  .card--left { left: 610px; top: 70px; }
  .card--back { left: 315px; top: 500px; background: var(--navy); }

  .band-top { position: absolute; left: 0; top: 0; width: 100%; height: 14px; background: var(--navy); }
  .band-bottom { position: absolute; left: 0; bottom: 0; width: 100%; height: 16px; background: var(--cyan); }

  .brand { position: absolute; top: 38px; display: flex; align-items: center; gap: 12px; }
  .card--centered .brand { left: 0; right: 0; justify-content: center; }
  .card--left .brand { left: 36px; }
  .brand-mark { width: 46px; height: 46px; border-radius: 50%; background: var(--navy); flex: none; }
  .brand-text { display: flex; flex-direction: column; }
  .brand-name { font-weight: 700; font-size: 31px; line-height: 1; color: var(--navy); letter-spacing: -0.3px; }
  .brand-tagline { font-size: 14px; color: var(--navy); margin-top: 4px; letter-spacing: 0.3px; }

  .person { position: absolute; top: 142px; }
  .card--centered .person { left: 0; right: 0; text-align: center; }
  .card--left .person { left: 36px; }
  .person-name { font-weight: 700; font-size: 18px; color: var(--ink); }
  .person-role { font-size: 15px; color: var(--ink); margin-top: 2px; }

  .contacts { position: absolute; left: 36px; top: 210px; list-style: none; }
  .contacts li { display: flex; align-items: center; gap: 10px; font-size: 14.5px; color: var(--ink); height: 22px; }
  .contacts svg { width: 14px; height: 14px; fill: var(--navy); flex: none; }

  .address { position: absolute; right: 40px; top: 208px; font-style: normal; font-size: 14.5px; line-height: 23px; color: var(--ink); }

  .back-pattern { position: absolute; inset: 0; background: radial-gradient(circle at 30% 30%, rgba(70, 90, 240, 0.55), transparent 55%), radial-gradient(circle at 80% 75%, rgba(60, 80, 235, 0.5), transparent 55%), var(--navy); }
  .back-brand { position: absolute; left: 40px; top: 118px; display: flex; align-items: center; gap: 14px; }
  .back-brand .brand-mark { background: var(--paper); width: 50px; height: 50px; }
  .back-brand .brand-name { color: var(--paper); font-size: 36px; }
  .website { position: absolute; left: 50px; top: 226px; display: flex; align-items: center; gap: 8px; color: var(--paper); font-size: 15px; letter-spacing: 0.8px; }
  .website svg { width: 16px; height: 16px; fill: none; stroke: var(--paper); stroke-width: 1.6; }
</style>
</head>
<body>

<svg width="0" height="0" style="position:absolute">
  <symbol id="icon-phone" viewBox="0 0 24 24"><path d="M3 9c0-3 4-5 9-5s9 2 9 5v2h-5V9c-1-1-7-1-8 0v2H3zM6 13h12l3 7H3z"/></symbol>
  <symbol id="icon-mobile" viewBox="0 0 24 24"><path d="M7 2h10a1 1 0 0 1 1 1v18a1 1 0 0 1-1 1H7a1 1 0 0 1-1-1V3a1 1 0 0 1 1-1zm1 3v12h8V5zm4 13.5a1.2 1.2 0 1 0 0 2.4 1.2 1.2 0 0 0 0-2.4z"/></symbol>
  <symbol id="icon-fax" viewBox="0 0 24 24"><path d="M6 2h12v6H6zM3 9h18v9h-3v-4H6v4H3zM7 15h10v7H7z"/></symbol>
  <symbol id="icon-mail" viewBox="0 0 24 24"><path d="M2 5h20v14H2zm2 2v.5l8 5.5 8-5.5V7l-8 5z"/></symbol>
</svg>

<!-- Front, centred layout -->
<section class="card card--front card--centered">
  <div class="band-top"></div>
  <div class="brand">
    <span class="brand-mark"></span>
    <div class="brand-text">
      <span class="brand-name">Calbrook Partners</span>
      <span class="brand-tagline">Coaching &amp; Consulting</span>
    </div>
  </div>
  <div class="person">
    <div class="person-name">Dr Elise Marlow, MBA, PhD</div>
    <div class="person-role">Managing Director</div>
  </div>
  <ul class="contacts">
    <li><svg><use href="#icon-phone"/></svg>+61 2 5550 1842</li>
    <li><svg><use href="#icon-mobile"/></svg>+61 400 555 218</li>
    <li><svg><use href="#icon-fax"/></svg>+61 2 5550 1843</li>
    <li><svg><use href="#icon-mail"/></svg>emarlow@calbrook.com.au</li>
  </ul>
  <address class="address">Suite 4B, Level 3<br>415 Harbour Road<br>Linfield, NSW<br>Australia, 2071</address>
  <div class="band-bottom"></div>
</section>

<!-- Front, left-aligned layout -->
<section class="card card--front card--left">
  <div class="band-top"></div>
  <div class="brand">
    <span class="brand-mark"></span>
    <div class="brand-text">
      <span class="brand-name">Calbrook Partners</span>
      <span class="brand-tagline">Coaching &amp; Consulting</span>
    </div>
  </div>
  <div class="person">
    <div class="person-name">Dr Elise Marlow, MBA, PhD</div>
    <div class="person-role">Managing Director</div>
  </div>
  <ul class="contacts">
    <li><svg><use href="#icon-phone"/></svg>+61 2 5550 1842</li>
    <li><svg><use href="#icon-mobile"/></svg>+61 400 555 218</li>
    <li><svg><use href="#icon-fax"/></svg>+61 2 5550 1843</li>
    <li><svg><use href="#icon-mail"/></svg>emarlow@calbrook.com.au</li>
  </ul>
  <address class="address">Suite 4B, Level 3<br>415 Harbour Road<br>Linfield, NSW<br>Australia, 2071</address>
  <div class="band-bottom"></div>
</section>

<!-- Back -->
<section class="card card--back">
  <div class="back-pattern" role="img" aria-label="Scattered blue circle pattern across the navy card back"></div>
  <div class="back-brand">
    <span class="brand-mark"></span>
    <span class="brand-name">Calbrook Partners</span>
  </div>
  <div class="website">
    <svg viewBox="0 0 24 24"><circle cx="12" cy="12" r="9"/><path d="M3 12h18M12 3c3 3 3 15 0 18M12 3c-3 3-3 15 0 18"/></svg>
    www.calbrook.com.au
  </div>
</section>

</body>
</html>
```